Visitenkarten-Design für italienisches Küchenschiff
Zielgruppe
Restaurantschiff Morvella
Aufgabenstellung
Wir sind ein italienische Küche Schiff auf der Binnenalster in Hamburg und wollen den schönen Blick und gerne auch die italienischen Farben widerspiegeln...ich brauche das einmal neutral für den normalen Gast....und würde das denn..wenn es denn gut wird...auch gerne individell mit m e i n e r Tel Nr und auch für meine führenden Mitarbeiter personalisieren...aber...zuerst natürlich das neutrale...dazu schicke ich die alte Karte mit dem auch alten Logo was nicht unbedingt verwendet werden muss...

```html
<!DOCTYPE html>
<html lang="de">
<head>
<meta charset="utf-8">
<title>Morvella Schiffsrestaurant – Visitenkarten</title>
<link href="https://fonts.googleapis.com/css2?family=Yanone+Kaffeesatz:wght@300&display=swap" rel="stylesheet">
<style>
  :root{
    --stage:#4a4a4a;
    --card-warm:#413d3c;
    --card-cool:#373737;
    --ink:#9c8d7a;
    --ink-logo:#8c7f6e;
    --rule:#6f655a;
    --green:#009a55;
    --white:#f7f7f7;
    --red:#b03537;
  }
  *{margin:0;padding:0;box-sizing:border-box}
  html,body{width:1200px;height:1200px;overflow:hidden;background:var(--stage)}
  body{position:relative;font-family:"Yanone Kaffeesatz",sans-serif;font-weight:300;color:var(--ink)}
  .card{position:absolute;width:510px;height:328px;box-shadow:3px 4px 6px rgba(0,0,0,.35);overflow:hidden}
  .card--warm{background:var(--card-warm)}
  .card--cool{background:var(--card-cool)}
  .front{left:61px}
  .back{left:628px}
  .row-1{top:36px}
  .row-2{top:632px}
  .abs{position:absolute;white-space:nowrap}

  .flag-side{position:absolute;left:0;top:0;width:14px;height:100%;display:flex;flex-direction:column}
  .flag-side span,.flag-bar span{flex:1}
  .green{background:var(--green)} .white{background:var(--white)} .red{background:var(--red)}

  .portrait{left:94px;top:45px;width:87px;height:126px;background:linear-gradient(180deg,#cfd6dc 0%,#7a8794 45%,#2e3136 100%)}
  .person{left:48px;top:172px;width:180px;text-align:center;font-size:20px;line-height:23px}
  .personal-contact{left:42px;top:262px;font-size:21px;line-height:22px}
  .personal-contact .label{display:inline-block;width:51px}
  .divider{left:259px;top:29px;width:1px;height:280px;background:var(--rule)}

  .brand{left:277px;top:88px}
  .brand-name{font-size:44px;line-height:44px;color:var(--ink-logo);letter-spacing:1px}
  .brand-mark{display:inline-block;width:12px;height:12px;border-radius:50%;background:var(--ink-logo);margin-left:8px;vertical-align:6px}
  .brand-sub{font-size:17px;letter-spacing:6.2px;color:var(--ink-logo);margin-top:-2px}
  .company{left:277px;top:161px;font-size:19px;line-height:19.5px}
  .company .gap{margin-top:5px}
  .company .label{display:inline-block;width:33px}

  .photo{left:22px;width:211px}
  .photo--salon{top:20px;height:129px;background:linear-gradient(180deg,#a98a5c 0%,#7d9ab0 28%,#5e7487 50%,#b5272b 72%,#e9e6e2 100%)}
  .photo--skyline{top:164px;height:125px;background:linear-gradient(180deg,#5a4e5a 0%,#6d5f6c 45%,#8b7a6a 68%,#2a2d3a 80%,#1c2030 100%)}
  .info{left:257px;width:231px}
  .heading{font-size:22px;line-height:24px}
  .text{font-size:19px;line-height:21.5px;margin-top:4px}
  .hours-row{display:flex;justify-content:space-between}
  .right{text-align:right}
  .short-rule{left:309px;top:155px;width:122px;height:1px;background:var(--rule)}
  .flag-bar{position:absolute;left:0;top:300px;width:100%;height:9px;display:flex}
</style>
</head>
<body>

<!-- Row 1 -->
<section class="card card--warm front row-1">
  <div class="flag-side"><span class="green"></span><span class="white"></span><span class="red"></span></div>
  <div class="abs portrait" role="img" aria-label="Porträtfoto des Mitarbeiters in Weste und Hemd"></div>
  <div class="abs person">Lorenzo Varenti<br>Capo</div>
  <div class="abs personal-contact"><span class="label">Tel:</span>+491 620 447 905<br><span class="label">E-Mail:</span>kalorix7@mailhaf.de</div>
  <div class="abs divider"></div>
  <div class="abs brand"><div class="brand-name">MORVELLA<span class="brand-mark"></span></div><div class="brand-sub">Schiffsrestaurant</div></div>
  <div class="abs company">Seekai 9b (Wasserseite)<br>20095 Hamburg<div class="gap">Kontakt</div><span class="label">Tel:</span>+49 040 / 58 14 63<br><span class="label">Fax:</span>+49 040 / 58 14 6<br>www.seeschiff-morvella.com<br>E-Mail: info@seeschiff-morvella.com</div>
</section>

<section class="card card--warm back row-1">
  <div class="abs photo photo--salon" role="img" aria-label="Foto des gedeckten Salons an Bord mit Blick auf die Binnenalster"></div>
  <div class="abs photo photo--skyline" role="img" aria-label="Foto der beleuchteten Uferpromenade bei Nacht"></div>
  <div class="abs info" style="top:45px"><div class="heading">Öffnungszeiten</div><div class="text hours-row"><span>Montag - Sonntag</span><span>12:00 - 23:00</span></div><div class="text right">Küche bis 22:00</div></div>
  <div class="abs short-rule"></div>
  <div class="abs info" style="top:178px"><div class="heading">Reservierungen</div><div class="text">Wir freuen uns auf Ihren Anruf oder<br>eine E-Mail:<br>reservierung@seeschiff-morvella.com</div></div>
  <div class="flag-bar"><span class="green"></span><span class="white"></span><span class="red"></span></div>
</section>

<!-- Row 2 -->
<section class="card card--cool front row-2">
  <div class="flag-side"><span class="green"></span><span class="white"></span><span class="red"></span></div>
  <div class="abs portrait" role="img" aria-label="Porträtfoto des Mitarbeiters in Weste und Hemd"></div>
  <div class="abs person">Lorenzo Varenti<br>Capo</div>
  <div class="abs personal-contact"><span class="label">Tel:</span>+491 620 447 905<br><span class="label">E-Mail:</span>kalorix7@mailhaf.de</div>
  <div class="abs divider"></div>
  <div class="abs brand"><div class="brand-name">MORVELLA<span class="brand-mark"></span></div><div class="brand-sub">Schiffsrestaurant</div></div>
  <div class="abs company">Seekai 9b (Wasserseite)<br>20095 Hamburg<div class="gap">Kontakt</div><span class="label">Tel:</span>+49 040 / 58 14 63<br><span class="label">Fax:</span>+49 040 / 58 14 6<br>www.seeschiff-morvella.com<br>E-Mail: info@seeschiff-morvella.com</div>
</section>

<section class="card card--cool back row-2">
  <div class="abs photo photo--salon" role="img" aria-label="Foto des gedeckten Salons an Bord mit Blick auf die Binnenalster"></div>
  <div class="abs photo photo--skyline" role="img" aria-label="Foto der beleuchteten Uferpromenade bei Nacht"></div>
  <div class="abs info" style="top:45px"><div class="heading">Öffnungszeiten</div><div class="text hours-row"><span>Montag - Sonntag</span><span>12:00 - 23:00</span></div><div class="text right">Küche bis 22:00</div></div>
  <div class="abs short-rule"></div>
  <div class="abs info" style="top:178px"><div class="heading">Reservierungen</div><div class="text">Wir freuen uns auf Ihren Anruf oder<br>eine E-Mail:<br>reservierung@seeschiff-morvella.com</div></div>
  <div class="flag-bar"><span class="green"></span><span class="white"></span><span class="red"></span></div>
</section>

</body>
</html>
```